Home care agency

Current website QTRBLOOMS.com. Need to update and reformat to different pages. use my info from my current website

Target Market(s)

adult children

Industry/Entity Type

Home Health

Coding

Coded - Design and coding required

Number of Pages Required

4 page

Font styles to use
Sans Serif

Colors
3276b5
33a6d7
3277b5
85cae6
85acd3

```html
<!DOCTYPE html>
<html lang="en">
<head>
<meta charset="utf-8">
<title>Quarter Blooms Health Services</title>
<link href="https://fonts.googleapis.com/css2?family=Great+Vibes&family=Poppins:wght@400;500;600&display=swap" rel="stylesheet">
<style>
:root{
  --blue-deep:#3276b5;
  --blue-mid:#3277b5;
  --blue-bright:#33a6d7;
  --blue-light:#85cae6;
  --blue-soft:#85acd3;
  --ink:#1f2430;
  --body:#555b66;
  --paper:#ffffff;
  --mist:#eef0f3;
  --script:"Great Vibes", cursive;
  --sans:"Poppins", sans-serif;
}
*{box-sizing:border-box;margin:0;padding:0}
html,body{width:1200px;height:3222px;overflow:hidden}
body{font-family:var(--sans);color:var(--ink);background:var(--paper);position:relative}
.abs{position:absolute}
.btn{position:absolute;display:flex;align-items:center;justify-content:center;border-radius:16px;color:#fff;font-size:10px;font-weight:600;letter-spacing:1px;text-transform:uppercase;text-decoration:none}
.btn--deep{background:var(--blue-deep)}
.btn--bright{background:var(--blue-bright)}
.script{font-family:var(--script);font-weight:400}

/* header */
.site-header{position:absolute;left:0;top:0;width:1200px;height:112px;background:var(--paper);z-index:3}
.brand{position:absolute;left:93px;top:5px;width:150px;height:150px;border-radius:50%;background:var(--paper);display:flex;flex-direction:column;align-items:center;justify-content:center;z-index:4;box-shadow:0 2px 6px rgba(0,0,0,.08)}
.brand__ring{position:absolute;inset:12px;border-radius:50%;border:3px solid var(--blue-soft)}
.brand__name{font-family:var(--sans);font-weight:500;color:var(--blue-deep);font-size:14px;text-align:center;line-height:1.3;letter-spacing:.5px}
.call{position:absolute;left:754px;top:30px;font-size:15px;font-weight:600;color:var(--ink);display:flex;align-items:center;gap:6px}
.call .script{color:var(--blue-bright);font-size:20px}
.main-nav a{position:absolute;top:74px;font-size:13px;font-weight:500;color:var(--ink);text-decoration:none}
.main-nav a.is-active{color:var(--blue-bright)}

/* hero */
.hero{position:absolute;left:0;top:112px;width:1200px;height:620px;background:linear-gradient(100deg,#4a3b33 0%,#7a6a5d 35%,#b9b6b1 60%,#8a7d72 80%,#5b4b40 100%)}
.hero__title{position:absolute;left:88px;top:262px;color:#fff;font-size:58px;line-height:1}
.hero__sub{position:absolute;left:88px;top:330px;color:#fff;font-size:38px;line-height:1}
.hero__text{position:absolute;left:88px;top:386px;width:470px;color:#fff;font-size:15px;line-height:18px}
.hero__dots span{position:absolute;left:1097px;width:12px;height:12px;border-radius:50%;border:1.5px solid #fff}
.hero__dots span.on::after{content:"";position:absolute;left:2px;top:2px;width:5px;height:5px;border-radius:50%;background:#fff}

/* about */
.about__halo{position:absolute;left:139px;top:783px;width:400px;height:400px;border-radius:50%;background:radial-gradient(circle,#fff 58%,#d7e8f3 70%,#f5f9fc 82%,#fff 100%)}
.about__photo{position:absolute;left:182px;top:826px;width:314px;height:314px;border-radius:50%;background:linear-gradient(160deg,#8b7a6e,#5d4f4b 55%,#e8e8e6)}
.about__title{position:absolute;left:616px;top:840px;font-size:46px;color:var(--ink);line-height:1}
.about__title b{font-family:var(--sans);font-weight:600;color:var(--blue-deep);font-size:36px;margin-left:6px}
.about__text{position:absolute;left:616px;width:480px;font-size:12px;line-height:19px;color:var(--body)}

/* services */
.services__title{position:absolute;left:0;width:1200px;top:1340px;text-align:center;font-size:50px;color:var(--ink)}
.card{position:absolute;top:1424px;width:319px;height:406px;background:var(--paper)}
.card__img{height:200px}
.card__title{position:absolute;left:24px;top:220px;font-size:16px;font-weight:500}
.card__list{position:absolute;left:24px;top:256px;list-style:none;font-size:12px;color:var(--body);line-height:19px}
.card__list li{display:flex;gap:8px;align-items:flex-start}
.card__list svg{flex:none;margin-top:5px}
.card .btn{left:24px;top:354px;width:96px;height:23px}

/* contact online */
.online__title{position:absolute;left:0;width:1200px;top:2030px;text-align:center;font-size:48px;color:var(--ink)}
.online__title span{color:var(--blue-bright)}
.online__text{position:absolute;left:0;width:1200px;top:2096px;text-align:center;font-size:18px;line-height:24px;color:#3b3f47}
.feature{position:absolute;top:2280px;width:300px;text-align:center}
.feature__badge{width:116px;height:116px;margin:0 auto;border-radius:50%;background:radial-gradient(circle,#fff 60%,#d3e6f2 72%,#fff 100%);display:flex;align-items:center;justify-content:center}
.feature__title{margin-top:24px;font-size:16px;font-weight:500}
.feature__text{margin-top:12px;font-size:12px;line-height:18px;color:var(--body)}
.feature--link .feature__title{color:var(--blue-bright)}
.feature--link .feature__text{text-decoration:underline;color:#4a5a78}

/* contact block */
.contact{position:absolute;left:0;top:2595px;width:1200px;height:627px;background:var(--mist)}
.contact__photo{position:absolute;left:0;top:2595px;width:345px;height:560px;background:linear-gradient(90deg,#6d5c52 0%,#a8968a 45%,rgba(238,240,243,0) 100%)}
.contact__title{position:absolute;left:352px;top:2680px;font-size:30px}
.contact__title span{color:var(--blue-deep)}
.contact__line{position:absolute;left:352px;font-size:13px;color:var(--ink)}
.contact__line b{color:var(--blue-deep);font-weight:500}
.map{position:absolute;left:679px;top:2651px;width:432px;height:295px;background:linear-gradient(135deg,#dfe9dc,#cfe3c9 50%,#e5ebe3)}

/* footer */
.social span{position:absolute;top:3059px;width:30px;height:30px;border-radius:50%;border:1.5px solid #fff}
.social span.on{background:#fff}
.footer-nav{position:absolute;left:0;width:1200px;top:3117px;display:flex;justify-content:center;gap:28px;color:#fff;font-size:13px;font-weight:500}
.copyright{position:absolute;left:0;width:1200px;top:3150px;text-align:center;color:#fff;font-size:10px}
</style>
</head>
<body>

<header class="site-header">
  <div class="call"><span class="script">Call Us:</span>
    <svg width="14" height="14" viewBox="0 0 24 24"><path fill="#33a6d7" d="M6.6 10.8a15 15 0 0 0 6.6 6.6l2.2-2.2c.3-.3.7-.4 1-.2 1.1.4 2.3.6 3.6.6.6 0 1 .4 1 1V20c0 .6-.4 1-1 1A17 17 0 0 1 3 4c0-.6.4-1 1-1h3.5c.6 0 1 .4 1 1 0 1.3.2 2.5.6 3.6.1.3 0 .7-.2 1z"/></svg>
    555-014-2290</div>
  <a class="btn btn--deep" style="left:984px;top:23px;width:127px;height:31px">Care Inquiry</a>
  <nav class="main-nav">
    <a class="is-active" style="left:495px">Home</a>
    <a style="left:590px">About Us</a>
    <a style="left:704px">Services</a>
    <a style="left:816px">Employment Application</a>
    <a style="left:1038px">Contact Us</a>
  </nav>
</header>
<div class="brand"><div class="brand__ring"></div><div class="brand__name">Quarter<br>Blooms</div></div>

<section class="hero" role="img" aria-label="Photo of a nurse in a white coat checking on an elderly man seated at home"></section>
<h1 class="hero__title script">Quarter Blooms</h1>
<div class="hero__sub script">Health Services</div>
<p class="hero__text">We individualize the care of our clients in order to provide the best care possible in their home.</p>
<a class="btn btn--bright" style="left:89px;top:458px;width:127px;height:31px">Contact Us</a>
<div class="hero__dots"><span style="top:310px"></span><span class="on" style="top:334px"></span><span style="top:359px"></span><span style="top:383px"></span></div>
<svg class="abs" style="left:0;top:560px" width="1200" height="180" viewBox="0 0 1200 180">
  <path fill="#3276b5" d="M0,33 C350,165 750,150 1200,40 L1200,180 L0,180Z"/>
  <path fill="#fff" d="M0,45 C350,190 750,172 1200,72 L1200,180 L0,180Z"/>
</svg>

<section class="about">
  <div class="about__halo"></div>
  <div class="about__photo" role="img" aria-label="Portrait of the owner, a registered nurse in a white coat"></div>
  <h2 class="about__title script">About<b>QTB</b></h2>
  <p class="about__text" style="top:913px">Quarter Blooms Health Services is owned and operated by Maren Castell. Maren is a registered nurse and has been in the health care system since 2001. She has specialized in home care, cardiology, trauma and critical care. She invests in future caregivers and has taught for the nursing programs at Eastbridge University, Bayside Health Institute, and Westmoor College.</p>
  <p class="about__text" style="top:1028px">All Quarter Blooms caregivers have extensive background checks and training regarding HIPAA compliance.</p>
  <a class="btn btn--deep" style="left:616px;top:1094px;width:128px;height:31px">Discover More</a>
</section>

<svg class="abs" style="left:0;top:1262px" width="1200" height="720" viewBox="0 0 1200 720">
  <path fill="#85cae6" d="M0,105 C350,15 800,-10 1200,82 L1200,600 C800,690 350,690 0,605Z"/>
  <path fill="#3276b5" d="M320,30 C620,-8 950,0 1200,58 L1200,82 C950,22 620,12 320,34Z"/>
  <path fill="#3276b5" d="M0,605 C350,690 800,690 1200,600 L1200,612 C800,712 350,712 0,622Z"/>
</svg>
<h2 class="services__title script">Our Services</h2>

<article class="card" style="left:88px">
  <div class="card__img" role="img" aria-label="Caregiver assisting a senior man in a wheelchair outdoors" style="background:linear-gradient(120deg,#a3845a,#d7c3a0 50%,#7a8a5a)"></div>
  <h3 class="card__title">Skilled Care Services</h3>
  <ul class="card__list">
    <li><svg width="10" height="8" viewBox="0 0 10 8"><path d="M1 4l3 3 5-6" stroke="#3276b5" stroke-width="1.5" fill="none"/></svg>Free Initial Nursing Assessment</li>
    <li><svg width="10" height="8" viewBox="0 0 10 8"><path d="M1 4l3 3 5-6" stroke="#3276b5" stroke-width="1.5" fill="none"/></svg>Medication Management</li>
    <li><svg width="10" height="8" viewBox="0 0 10 8"><path d="M1 4l3 3 5-6" stroke="#3276b5" stroke-width="1.5" fill="none"/></svg>Wound Care</li>
    <li><svg width="10" height="8" viewBox="0 0 10 8"><path d="M1 4l3 3 5-6" stroke="#3276b5" stroke-width="1.5" fill="none"/></svg>Injections</li>
  </ul>
  <a class="btn btn--bright">Read More</a>
</article>
<article class="card" style="left:440px">
  <div class="card__img" role="img" aria-label="Nurse with a tablet talking with a senior woman" style="background:linear-gradient(120deg,#8aa56a,#e7e1d6 50%,#c9c0b3)"></div>
  <h3 class="card__title">Non-Medical Services</h3>
  <ul class="card__list">
    <li><svg width="10" height="8" viewBox="0 0 10 8"><path d="M1 4l3 3 5-6" stroke="#3276b5" stroke-width="1.5" fill="none"/></svg>Live-In Care</li>
    <li><svg width="10" height="8" viewBox="0 0 10 8"><path d="M1 4l3 3 5-6" stroke="#3276b5" stroke-width="1.5" fill="none"/></svg>Respite Care</li>
    <li><svg width="10" height="8" viewBox="0 0 10 8"><path d="M1 4l3 3 5-6" stroke="#3276b5" stroke-width="1.5" fill="none"/></svg>Assisting with Daily Living Activities</li>
    <li><svg width="10" height="8" viewBox="0 0 10 8"><path d="M1 4l3 3 5-6" stroke="#3276b5" stroke-width="1.5" fill="none"/></svg>Meal Preparations</li>
  </ul>
  <a class="btn btn--deep">Read More</a>
</article>
<article class="card" style="left:792px">
  <div class="card__img" role="img" aria-label="Smiling senior couple embracing" style="background:linear-gradient(120deg,#e9ebec,#bfc3c7 50%,#8f9aa6)"></div>
  <h3 class="card__title">Client Benefits</h3>
  <ul class="card__list">
    <li><svg width="10" height="8" viewBox="0 0 10 8"><path d="M1 4l3 3 5-6" stroke="#3276b5" stroke-width="1.5" fill="none"/></svg><span>Continuity of care with same caregiver<br>for each client on a regular basis.</span></li>
    <li><svg width="10" height="8" viewBox="0 0 10 8"><path d="M1 4l3 3 5-6" stroke="#3276b5" stroke-width="1.5" fill="none"/></svg><span>Open communication with owner by<br>phone or email.</span></li>
  </ul>
  <a class="btn btn--bright">Read More</a>
</article>

<h2 class="online__title script">Contact <span>Online</span></h2>
<p class="online__text">To contact us online, please fill out the care inquiry form and<br>you will be contacted within 24-48 hours.</p>
<a class="btn btn--bright" style="left:536px;top:2171px;width:128px;height:31px">Care Inquiry</a>

<div class="feature" style="left:92px">
  <div class="feature__badge"><svg width="44" height="44" viewBox="0 0 44 44"><path d="M17 6h10v11h11v10H27v11H17V27H6V17h11z" fill="none" stroke="#85acd3" stroke-width="2.5"/></svg></div>
  <h3 class="feature__title">Why Choose Home Care?</h3>
  <p class="feature__text">Home care is a cost-effective option that<br>allows clients the ability to receive one-on-one<br>care in the comfort of their ...</p>
</div>
<div class="feature feature--link" style="left:449px">
  <div class="feature__badge"><svg width="44" height="44" viewBox="0 0 44 44"><rect x="5" y="8" width="34" height="30" rx="3" fill="none" stroke="#3276b5" stroke-width="2.5"/><path d="M5 16h34M13 4v8M31 4v8" stroke="#3276b5" stroke-width="2.5"/><circle cx="30" cy="29" r="6" fill="#fff" stroke="#3276b5" stroke-width="2"/><path d="M30 26v3h2" stroke="#3276b5" stroke-width="1.5" fill="none"/></svg></div>
  <h3 class="feature__title">Care Schedule/Frequency</h3>
  <p class="feature__text">Quarter Blooms non-medical visits<br>require a four hour minimum visit, here are no<br>weekly minimum for medical ...</p>
</div>
<div class="feature" style="left:803px">
  <div class="feature__badge"><svg width="44" height="44" viewBox="0 0 44 44"><rect x="4" y="12" width="30" height="20" rx="3" fill="none" stroke="#85acd3" stroke-width="2.5"/><rect x="10" y="17" width="30" height="20" rx="3" fill="#fff" stroke="#85acd3" stroke-width="2.5"/><path d="M10 23h30" stroke="#85acd3" stroke-width="2.5"/></svg></div>
  <h3 class="feature__title">Payment Options</h3>
  <p class="feature__text">Quarter Blooms currently accepts check<br>for service payments (with plans for online<br>payments late 2018.)</p>
</div>

<section class="contact"></section>
<div class="contact__photo" role="img" aria-label="Portrait of the owner smiling in a white coat"></div>
<h2 class="contact__title script">Contact <span>Us</span></h2>
<p class="contact__line" style="top:2733px;font-size:15px;font-weight:600"><span class="script" style="color:var(--blue-deep);font-size:20px;font-weight:400">Call:</span> 555-014-2290</p>
<p class="contact__line" style="top:2762px"><b>Email:</b> info@qtrblooms.com</p>
<p class="contact__line" style="top:2810px"><b>Quarter Blooms Health Services</b></p>
<p class="contact__line" style="top:2834px">PO Box 48 Harborview, MA 02099</p>
<a class="btn btn--deep" style="left:352px;top:2881px;width:128px;height:31px">Care Inquiry</a>
<div class="map" role="img" aria-label="Map of the service area south-west of the city"></div>

<svg class="abs" style="left:0;top:2960px" width="1200" height="262" viewBox="0 0 1200 262">
  <path fill="#85cae6" d="M0,150 C300,15 800,10 1200,112 L1200,130 C800,30 300,35 0,165Z"/>
  <path fill="#3276b5" d="M0,160 C300,30 800,28 1200,125 L1200,262 L0,262Z"/>
</svg>
<div class="social" aria-label="Social links">
  <span style="left:526px"></span><span class="on" style="left:565px"></span><span style="left:604px"></span><span style="left:642px"></span>
</div>
<nav class="footer-nav"><span>Home</span><span>I</span><span>About Us</span><span>I</span><span>Services</span><span>I</span><span>Employment Application</span><span>I</span><span>Contact Us</span></nav>
<p class="copyright">© 2019 Quarter Blooms Health Services. All Right Reserved</p>

</body>
</html>
```